Loopwave template for supermarket

I need a new fresh Loopwave template in which I can paste an image that changes depending on the content of the Loopwave post. I need to be able to change the design in Adobe Photoshop. It concerns the LW page of a local supermarket.
I once made a template myself, but I'm not satisfied with it.
Check the supermarket's website to see the supermarket's color scheme and style. The supermarket is a forerunner in the field of fresh products from local suppliers and has a wide range of organic products.
The slogan of the supermarket is 'At VENK we bring fresh meals, our street and one another'. The supermarket has a strong bond with the neighborhood and the inhabitants.
I have added my self-made template as an example. At the bottom right is the name of the owners of the supermarket.

```html
<!DOCTYPE html>
<html lang="en">
<head>
<meta charset="utf-8">
<title>VENK Loopwave post template</title>
<link href="https://fonts.googleapis.com/css2?family=Montserrat:wght@500;700;800&display=swap" rel="stylesheet">
<style>
  :root {
    --green-top: #66bf14;
    --green-bottom: #4f9f0c;
    --green-dark: #3f8a08;
    --brand-green: #5fae1e;
    --white: #ffffff;
    --produce-orange: #ef8a1c;
    --produce-red: #b3213a;
    --produce-pink: #e8709a;
  }
  * { margin: 0; padding: 0; box-sizing: border-box; }
  html, body { width: 1200px; height: 1200px; overflow: hidden; }
  body { font-family: "Montserrat", Arial, sans-serif; }
  .post {
    position: relative;
    width: 1200px;
    height: 1200px;
    background: linear-gradient(180deg, var(--green-top) 0%, var(--green-bottom) 100%);
    overflow: hidden;
  }
  .headline {
    position: absolute;
    top: 72px;
    left: 0;
    width: 1170px;
    text-align: center;
    color: var(--white);
    font-weight: 700;
    font-size: 40px;
    line-height: 54px;
  }
  .photo-frame {
    position: absolute;
    left: 0;
    top: 240px;
    width: 1200px;
    height: 760px;
  }
  .slogan {
    position: absolute;
    left: 68px;
    top: 1052px;
    color: var(--white);
    font-weight: 500;
    font-size: 25px;
    line-height: 42px;
  }
  .slogan strong { font-weight: 800; }
  .owner-panel {
    position: absolute;
    left: 638px;
    top: 998px;
    width: 547px;
    height: 187px;
    background: var(--white);
    border-radius: 94px 0 0 94px;
    display: flex;
    flex-direction: column;
    align-items: center;
    justify-content: center;
    gap: 8px;
    color: var(--brand-green);
    padding-left: 40px;
  }
  .brand-name {
    display: flex;
    align-items: center;
    gap: 14px;
    font-weight: 800;
    font-size: 46px;
    line-height: 1;
  }
  .brand-dot {
    width: 22px;
    height: 22px;
    border-radius: 50%;
    background: var(--brand-green);
  }
  .owners {
    font-weight: 700;
    font-size: 24px;
  }
</style>
</head>
<body>
  <main class="post">
    <h1 class="headline">Lorem ipsum dolor nibh diam sit amet<br>consectetur adipiscing elit</h1>

    <svg class="photo-frame" viewBox="0 0 1200 760" width="1200" height="760">
      <defs>
        <linearGradient id="produceTones" x1="0" y1="0" x2="1" y2="1">
          <stop offset="0" stop-color="#e8709a"/>
          <stop offset="0.3" stop-color="#ef8a1c"/>
          <stop offset="0.55" stop-color="#b3213a"/>
          <stop offset="0.8" stop-color="#ef8a1c"/>
          <stop offset="1" stop-color="#e8709a"/>
        </linearGradient>
      </defs>
      <path class="arch-band" d="M15 78 Q600 -30 1185 78 L1185 96 Q600 -10 15 96 Z" fill="#3f8a08"/>
      <path class="post-image" role="img" aria-label="Post photo: supermarket shelves stacked with oranges, red apples and pink-wrapped fruit"
            d="M15 92 Q600 -12 1185 92 L1185 758 L15 758 Z" fill="url(#produceTones)"/>
    </svg>

    <p class="slogan">At <strong>VENK</strong> we bring <strong>fresh meals</strong>,<br>our street and one another</p>

    <div class="owner-panel">
      <div class="brand-name"><span class="brand-dot"></span><span>VENK</span></div>
      <div class="owners">VENK Mark en Lotte de Vries</div>
    </div>
  </main>
</body>
</html>
```